Harbor Lawn and Stoneworks Flyer/Brochure

Flyer/Brochure for artificial turf and paver company. Photos and txt<br/>Specializes in Turf, Pavers, Patio, Decorative Rock, Hardscape, Landscape Design.

Target Market(s)

Homeowners

Industry/Entity Type

Construction

Font styles to use
Sans Serif

Colors
9bcb3c

Requirements
Must have
• Photos, we will provide as well as logo
• phone number and email address
• similar branding as website
• www.harborlsw.com
Nice to have
• eye catching not too busy
• clean and easy to read
• Hi! Please see photos on our instagram - there are a couple shots that may be better than the website there.
• Also, photo of dog on turf. Please mention kid -play turf and pet turf is available or something like "your pup will love our pet turf"
• Add- "Ask us about our specials"
• phone number is 800-413-2786

```html
<!DOCTYPE html>
<html lang="en">
<head>
<meta charset="utf-8">
<title>Harbor Lawn and Stoneworks Flyers</title>
<link href="https://fonts.googleapis.com/css2?family=Open+Sans:wght@400;600;700&family=Ubuntu:wght@500;700&display=swap" rel="stylesheet">
<style>
:root{
  --green:#7dc242;
  --green-deep:#5fa52c;
  --ink:#222;
  --text:#555;
  --footer:#3a3a3c;
  --page:#e6e6e4;
  --white:#fff;
}
*{box-sizing:border-box;margin:0;padding:0}
html,body{width:1200px;height:770px;overflow:hidden;background:var(--page)}
body{position:relative;font-family:"Open Sans",Arial,sans-serif}
.flyer{position:absolute;top:60px;width:500px;height:650px;background:var(--white);overflow:hidden;box-shadow:0 4px 14px rgba(0,0,0,.18)}
.flyer--turf{left:70px}
.flyer--pavers{left:630px}
.abs{position:absolute}
.brand{left:24px;top:14px;display:flex;align-items:center;gap:9px}
.brand-mark{width:16px;height:16px;background:var(--green);flex:none}
.brand-name{font-family:"Ubuntu",Arial,sans-serif;font-weight:700;font-size:17px;line-height:19px;color:var(--ink);white-space:nowrap;text-transform:uppercase}
.license{right:22px;top:18px;font-size:6px;color:#777}
.consult{right:22px;top:30px;font-family:"Ubuntu",Arial,sans-serif;font-weight:500;font-size:12px;color:var(--ink)}
.header-band{left:0;top:56px;width:500px;height:17px}
.hero{left:0;top:73px;width:500px}
.flyer--turf .hero{height:255px;background:linear-gradient(160deg,#5d6b3c 0%,#a99c7c 35%,#c8b89a 55%,#5e7a2e 80%,#3e5a1e 100%)}
.flyer--pavers .hero{height:240px;background:linear-gradient(170deg,#9c7358 0%,#b88b6c 30%,#8c6a55 55%,#a07a64 80%,#6f5646 100%)}
.hero-swoosh{left:0;width:500px;height:40px}
.headline{left:24px;top:140px;font-family:"Ubuntu",Arial,sans-serif;font-weight:700;font-size:21px;line-height:26px;color:var(--white);text-transform:uppercase;text-shadow:0 1px 3px rgba(0,0,0,.45)}
.headline-rule{left:24px;top:224px;width:70px;height:2px;background:var(--green)}
.tagline{left:22px;top:233px;font-size:11px;line-height:16px;color:var(--white);font-weight:600;text-shadow:0 1px 2px rgba(0,0,0,.5)}
.section-title{font-family:"Ubuntu",Arial,sans-serif;font-weight:700;font-size:12.5px;color:var(--ink);text-transform:uppercase}
.body-copy{font-size:9.6px;line-height:12.8px;color:var(--text);text-align:justify}
.body-copy--turf{font-size:9.2px;line-height:12.2px}
.photo{border-radius:3px;overflow:hidden}
.photo-label{position:absolute;bottom:4px;font-size:7px;font-weight:700;color:var(--white)}
.spec-title{font-family:"Ubuntu",Arial,sans-serif;font-weight:500;font-size:12px;color:var(--ink)}
.spec-item{display:flex;align-items:center;gap:6px;font-size:11.5px;color:#444}
.spec-icon{width:24px;height:24px;border-radius:50%;background:var(--green);display:flex;align-items:center;justify-content:center}
.badges{display:flex;gap:6px}
.badge{width:34px;height:34px;border-radius:50%;background:radial-gradient(circle,#f3c63e 55%,#c9962a 58%,#e9b938 100%)}
.footer{left:0;top:614px;width:500px;height:36px}
.footer-contact{left:24px;top:624px;font-family:"Ubuntu",Arial,sans-serif;font-weight:700;font-size:12.5px;color:var(--white);letter-spacing:.3px}
.footer-phone{right:20px;top:622px;display:flex;align-items:center;gap:8px;font-family:"Ubuntu",Arial,sans-serif;font-weight:700;font-size:14px;color:var(--white);letter-spacing:.5px}
.service-card{width:148px;height:126px;border-radius:3px;overflow:hidden}
.service-card .card-photo{height:78px}
.service-card .card-base{position:absolute;left:0;top:78px;width:148px;height:48px;background:var(--green)}
.service-card .card-icon{position:absolute;left:50%;top:60px;width:40px;height:40px;margin-left:-20px;border-radius:50%;background:var(--green);border:3px solid var(--white);display:flex;align-items:center;justify-content:center}
.service-card .card-label{position:absolute;left:0;bottom:6px;width:100%;text-align:center;font-family:"Ubuntu",Arial,sans-serif;font-weight:700;font-size:9.5px;color:var(--white);letter-spacing:.6px}
.subhead{font-family:"Ubuntu",Arial,sans-serif;font-weight:700;font-size:13px;color:var(--ink)}
</style>
</head>
<body>

<section class="flyer flyer--turf">
  <div class="abs brand"><span class="brand-mark"></span><span class="brand-name">Harbor Lawn<br>and Stoneworks</span></div>
  <div class="abs license">CSLB#: 2047719</div>
  <div class="abs consult">SCHEDULE FREE CONSULTATION</div>
  <svg class="abs header-band" viewBox="0 0 500 17" preserveAspectRatio="none"><polygon points="285,17 300,0 500,0 500,17" fill="var(--green)"/></svg>

  <div class="abs hero" role="img" aria-label="Terraced backyard with retaining walls, stone steps, gravel paths and green turf with plants in the foreground"></div>
  <svg class="abs hero-swoosh" style="top:300px" viewBox="0 0 500 40" preserveAspectRatio="none">
    <path d="M0,0 Q250,28 500,0 L500,40 L0,40 Z" fill="var(--green)"/>
    <path d="M0,10 Q250,34 500,8 L500,40 L0,40 Z" fill="var(--white)"/>
  </svg>
  <h1 class="abs headline">Make your<br>outdoor living<br>vision a&nbsp; reality</h1>
  <div class="abs headline-rule"></div>
  <p class="abs tagline">Effortless Outdoor Transformations/<br>Creative, Elegant, Sustainable</p>

  <h2 class="abs section-title" style="left:23px;top:357px">Synthetic Turf</h2>
  <p class="abs body-copy body-copy--turf" style="left:24px;top:375px;width:232px">Harbor Lawn and Stoneworks specializes in pet friendly PlushLawn synthetic grass and turf products with CleanShield antimicrobial technology that are specifically made for your pet and provide an odorless, soft-to-the-touch turf that stays clean and green year round. We are expert at providing an installation process that considers drainage and ammonia neutralization as well.</p>

  <div class="abs photo" style="left:269px;top:357px;width:213px;height:119px;display:flex">
    <div role="img" aria-label="Backyard before installation with bare dirt beside a house" style="width:50%;height:100%;background:linear-gradient(180deg,#c9ccd0 0%,#b3ada2 40%,#9b8a72 100%);position:relative"><span class="photo-label" style="left:4px">BEFORE</span></div>
    <div role="img" aria-label="Same backyard after installation with green turf and gravel border" style="width:50%;height:100%;background:linear-gradient(180deg,#c4c8cc 0%,#a9a8a2 40%,#4d7d33 62%,#8b8a86 100%);position:relative"><span class="photo-label" style="left:6px">AFTER</span></div>
  </div>
  <div class="abs photo" role="img" aria-label="Turf lawn with concrete edging" style="left:269px;top:489px;width:69px;height:68px;background:linear-gradient(180deg,#a7b0b5,#4f8a33 55%,#8f948f)"></div>
  <div class="abs photo" role="img" aria-label="Pool surrounded by synthetic turf" style="left:341px;top:489px;width:69px;height:68px;background:linear-gradient(180deg,#9fb6c6,#5f8f3a 45%,#3aa6c8 65%,#4b8131)"></div>
  <div class="abs photo" role="img" aria-label="Turf strip beside a covered patio" style="left:413px;top:489px;width:69px;height:68px;background:linear-gradient(90deg,#c9c1b4,#4f8a33 50%,#3f7a2a)"></div>

  <h3 class="abs spec-title" style="left:23px;top:503px">Specializes in:</h3>
  <div class="abs spec-item" style="left:24px;top:522px"><span class="spec-icon"><svg width="14" height="14" viewBox="0 0 14 14"><path d="M7 13 L4 3 M7 13 L7 1 M7 13 L10 3" stroke="#fff" stroke-width="1.6" fill="none"/></svg></span>Turf</div>
  <div class="abs spec-item" style="left:24px;top:551px"><span class="spec-icon"><svg width="14" height="14" viewBox="0 0 14 14"><polygon points="7,1 13,7 7,13 1,7" fill="#fff"/></svg></span>Pavers</div>
  <div class="abs spec-item" style="left:24px;top:580px"><span class="spec-icon"><svg width="14" height="14" viewBox="0 0 14 14"><path d="M1 5 L7 1 L13 5 Z M2 6 H12 V13 H2 Z" fill="#fff"/></svg></span>Patio</div>
  <div class="abs spec-item" style="left:136px;top:522px"><span class="spec-icon"><svg width="14" height="14" viewBox="0 0 14 14"><rect x="1" y="3" width="6" height="4" fill="#fff"/><rect x="1" y="8" width="5" height="4" fill="#fff"/><rect x="7" y="8" width="6" height="4" fill="#fff"/></svg></span>Decorative Rock</div>
  <div class="abs spec-item" style="left:136px;top:551px"><span class="spec-icon"><svg width="14" height="14" viewBox="0 0 14 14"><rect x="5" y="1" width="4" height="4" fill="#fff"/><rect x="1" y="5" width="4" height="4" fill="#fff"/><rect x="9" y="5" width="4" height="4" fill="#fff"/><rect x="5" y="9" width="4" height="4" fill="#fff"/></svg></span>Hardscape</div>
  <div class="abs spec-item" style="left:136px;top:580px"><span class="spec-icon"><svg width="14" height="14" viewBox="0 0 14 14"><circle cx="5" cy="5" r="3" fill="#fff"/><circle cx="9" cy="9" r="3" fill="#fff"/></svg></span>Landscape Design</div>

  <div class="abs badges" style="left:368px;top:566px"><span class="badge"></span><span class="badge"></span><span class="badge"></span></div>

  <svg class="abs footer" viewBox="0 0 500 36" preserveAspectRatio="none"><rect width="500" height="36" fill="var(--footer)"/><polygon points="300,0 500,0 500,36 320,36" fill="var(--green)"/></svg>
  <div class="abs footer-contact">info@harborlsw.com &nbsp;|&nbsp; www.harborlsw.com</div>
  <div class="abs footer-phone"><svg width="10" height="15" viewBox="0 0 10 15"><rect x="1" y="1" width="8" height="13" rx="1.5" stroke="#fff" stroke-width="1.5" fill="none"/></svg>800-413-2786</div>
</section>

<section class="flyer flyer--pavers">
  <div class="abs brand"><span class="brand-mark"></span><span class="brand-name">Harbor Lawn<br>and Stoneworks</span></div>
  <div class="abs license">CSLB#: 2047719</div>
  <div class="abs consult">SCHEDULE FREE CONSULTATION</div>
  <svg class="abs header-band" viewBox="0 0 500 17" preserveAspectRatio="none"><polygon points="285,17 300,0 500,0 500,17" fill="var(--green)"/></svg>

  <div class="abs hero" role="img" aria-label="Paver patio with a round stone fire pit, curved seating wall and outdoor furniture against a block wall"></div>
  <svg class="abs hero-swoosh" style="top:285px" viewBox="0 0 500 40" preserveAspectRatio="none">
    <path d="M0,0 Q250,28 500,0 L500,40 L0,40 Z" fill="var(--green)"/>
    <path d="M0,10 Q250,34 500,8 L500,40 L0,40 Z" fill="var(--white)"/>
  </svg>
  <h1 class="abs headline">Make your<br>outdoor living<br>vision a&nbsp; reality</h1>
  <div class="abs headline-rule"></div>
  <p class="abs tagline">Effortless Outdoor Transformations/<br>Creative, Elegant, Sustainable</p>

  <h2 class="abs section-title" style="left:23px;top:340px">Interlocking Paver Systems</h2>
  <p class="abs body-copy" style="left:24px;top:359px;width:458px">With Interlocking Stone Pavers, you can create new custom areas for outdoor living or embellish any area that needs a well deserved facelift. These versatile and functional systems are well suited to enhance and overlay driveways, create or expand patios, walkways and pool decks, and add layers of interest with retaining walls.</p>

  <div class="abs service-card" style="left:24px;top:419px">
    <div class="card-photo" role="img" aria-label="Grey interlocking paver stones" style="background:linear-gradient(135deg,#8a8d93,#b6b8bc 50%,#7c7f85)"></div>
    <div class="card-base"></div>
    <div class="card-icon"><svg width="18" height="18" viewBox="0 0 18 18"><rect x="2" y="2" width="6" height="6" fill="#fff"/><rect x="10" y="2" width="6" height="6" fill="#fff"/><rect x="2" y="10" width="6" height="6" fill="#fff"/><rect x="10" y="10" width="6" height="6" fill="#fff"/></svg></div>
    <div class="card-label">PAVER SYSTEMS</div>
  </div>
  <div class="abs service-card" style="left:176px;top:419px">
    <div class="card-photo" role="img" aria-label="Backyard pool edged with synthetic turf" style="background:linear-gradient(180deg,#c6d3dc,#6f9a45 45%,#3aa6c8 70%,#5a8f35)"></div>
    <div class="card-base"></div>
    <div class="card-icon"><svg width="18" height="18" viewBox="0 0 18 18"><path d="M9 16 L5 4 M9 16 L9 2 M9 16 L13 4 M9 16 L2 8 M9 16 L16 8" stroke="#fff" stroke-width="1.5" fill="none"/></svg></div>
    <div class="card-label">SYNTHETIC TURF</div>
  </div>
  <div class="abs service-card" style="left:328px;top:419px">
    <div class="card-photo" role="img" aria-label="White pergola patio cover beside a stucco house" style="background:linear-gradient(180deg,#a9c4de,#e8e4dc 45%,#5f8f3a)"></div>
    <div class="card-base"></div>
    <div class="card-icon"><svg width="18" height="18" viewBox="0 0 18 18"><path d="M2 7 L9 2 L16 7 Z" fill="#fff"/><path d="M4 8 V16 M14 8 V16 M9 8 V16" stroke="#fff" stroke-width="1.6"/></svg></div>
    <div class="card-label">PATIO COVERS</div>
  </div>

  <h3 class="abs subhead" style="left:23px;top:564px">Endless Possibilities</h3>
  <p class="abs body-copy" style="left:24px;top:582px;width:300px;text-align:left">We work with a wide variety of manufacturers to offer extensive and far reaching choices!</p>
  <div class="abs badges" style="left:368px;top:566px"><span class="badge"></span><span class="badge"></span><span class="badge"></span></div>

  <svg class="abs footer" viewBox="0 0 500 36" preserveAspectRatio="none"><rect width="500" height="36" fill="var(--footer)"/><polygon points="300,0 500,0 500,36 320,36" fill="var(--green)"/></svg>
  <div class="abs footer-contact">info@harborlsw.com &nbsp;|&nbsp; www.harborlsw.com</div>
  <div class="abs footer-phone"><svg width="10" height="15" viewBox="0 0 10 15"><rect x="1" y="1" width="8" height="13" rx="1.5" stroke="#fff" stroke-width="1.5" fill="none"/></svg>800-413-2786</div>
</section>

</body>
</html>
```